Menu Re-Design for The Marbrook a british eatery in spanish holiday resort

Looking for a new design for our breakfast and lunch menu....

I have included some pictures of a few menus I like the feel of File No 1,2,3,4,5..... but am open to any ideas you may have....

The menu is to be double sided consisting of a front design with actual menu on reverse....

I have also included the relevant text files you will require...

We do not have a logo or set colour scheme to follow...

Target Market(s)

Predominantly British holidaymakers in popular Spanish resort....

Requirements
Must have
• Menu to be A3 and double sided, split between either a front page design and menu on reverse, or menu divided between both sides....
• Company Name:- The Marbrook
Nice to have
• Fun and Bold design whilst maintaining a feel of quality....
Should not have
• Please avoid the use of any food photography....

```html
<!DOCTYPE html>
<html lang="en">
<head>
<meta charset="utf-8">
<title>The Marbrook – Daytime Menu</title>
<link href="https://fonts.googleapis.com/css2?family=Alfa+Slab+One&family=Oswald:wght@500;700&family=Archivo+Black&family=Open+Sans:wght@400;600&display=swap" rel="stylesheet">
<style>
  :root{
    --maroon:#7a1f1c;
    --rust:#c2461f;
    --orange:#e8732a;
    --olive:#c5a62c;
    --mustard:#c6ac45;
    --mustard-dark:#9c8630;
    --cream:#f3eac6;
    --cream-text:#efe3b8;
    --brown:#a4532f;
    --ink:#1d1a17;
    --paper:#ffffff;
    --stage:#2e2823;
  }
  *{box-sizing:border-box;margin:0;padding:0}
  html,body{width:1200px;height:800px;overflow:hidden;background:var(--stage)}
  body{position:relative;font-family:"Open Sans",sans-serif;color:var(--ink)}

  .lights{position:absolute;left:0;right:0;top:0;height:16px;
    background:linear-gradient(180deg,rgba(255,255,255,.55),rgba(255,255,255,0));}

  /* ---------- front cover ---------- */
  .cover{position:absolute;left:40px;top:30px;width:430px;height:740px;
    background:radial-gradient(ellipse at 50% 45%,var(--mustard) 55%,var(--mustard-dark) 120%);overflow:hidden}
  .cover__name{position:absolute;left:0;right:0;top:250px;text-align:center;color:var(--maroon);
    font-family:"Alfa Slab One",serif;font-weight:400;font-size:50px;line-height:1}
  .cover__slogan{position:absolute;left:0;right:0;top:500px;text-align:center;font-family:"Alfa Slab One",serif;font-size:58px;line-height:1.05;letter-spacing:1px}
  .cover__slogan span{display:block;text-shadow:4px 4px 0 rgba(0,0,0,.25)}
  .cover__slogan .eat,.cover__slogan .happy{color:var(--maroon)}
  .cover__slogan .drink{color:var(--cream-text)}

  /* ---------- menu page ---------- */
  .menu{position:absolute;left:500px;top:30px;width:670px;height:740px;overflow:hidden;background:var(--paper);padding:24px 16px 10px 16px;font-size:7.4px;line-height:1.28}
  .menu__head{display:flex;align-items:center;gap:14px;height:56px;margin-top:6px}
  .menu__brand{font-family:"Alfa Slab One",serif;color:var(--maroon);font-size:22px;line-height:1;width:196px;white-space:nowrap}
  .menu__brand small{font-size:14px}
  .menu__title{font-family:"Alfa Slab One",serif;font-weight:400;color:var(--paper);-webkit-text-stroke:1.2px var(--brown);text-shadow:2px 2px 0 var(--brown);font-size:34px;line-height:1;letter-spacing:1px}
  .menu__served{font-family:"Oswald",sans-serif;font-weight:700;color:var(--orange);font-size:11px;line-height:1.05}
  .menu__body{display:grid;grid-template-columns:196px 1fr;gap:12px;margin-top:6px}
  .col{display:flex;flex-direction:column;gap:6px}
  .col--right{line-height:1.42;gap:9px}
  .col--right .col{gap:9px}
  .split{display:grid;grid-template-columns:1fr 1fr;gap:12px}

  .h{font-family:"Oswald",sans-serif;font-weight:700;color:var(--rust);font-size:18px;line-height:1.05;text-transform:uppercase}
  .h--slab{font-family:"Alfa Slab One",serif;text-transform:none;font-weight:400}
  .h--light{color:var(--paper)}
  .h--maroon{color:var(--maroon)}
  .note{font-weight:600;font-size:6.6px;line-height:1.3}
  .items b{font-family:"Archivo Black",sans-serif;font-weight:400}
  .items li{list-style:none}
  .items .p{font-weight:400;font-size:6.6px}
  .desc{font-size:6.4px;color:#444}

  .panel{padding:6px 8px}
  .panel--olive{background:var(--olive);color:var(--paper)}
  .panel--cream{background:var(--cream);border:1.5px solid var(--orange)}
  .panel--brown{background:var(--brown);color:var(--paper)}

  .breakfasts{display:grid;grid-template-columns:1fr 1fr;gap:4px 12px}
  .breakfasts .intro{align-self:center}
  .breakfasts .foot{grid-column:1/3}
  .rule{border-bottom:1px solid var(--orange);padding-bottom:6px}
  .extras{display:grid;grid-template-columns:1fr 1fr;font-size:6.6px}
</style>
</head>
<body>

<section class="cover" aria-label="Menu front cover">
  <div class="lights" role="img" aria-label="String of festoon lights along the top edge"></div>
  <h1 class="cover__name">The Marbrook</h1>
  <p class="cover__slogan"><span class="eat">EAT</span><span class="drink">DRINK</span><span class="happy">BE HAPPY</span></p>
</section>

<section class="menu" aria-label="Daytime menu">
  <div class="lights" role="img" aria-label="String of festoon lights along the top edge"></div>
  <header class="menu__head">
    <div class="menu__brand"><small>The </small>Marbrook</div>
    <h2 class="menu__title">DAYTIME MENU</h2>
    <div class="menu__served">SERVED<br>UNTIL<br>5PM</div>
  </header>

  <div class="menu__body">
    <div class="col">
      <div>
        <h3 class="h">Build <span class="h--maroon">your own</span></h3>
        <p class="note">Minimum order of 3.50 euros</p>
        <ul class="items">
          <li><b>Sausage</b> <span class="p">1.00</span></li>
          <li><b>Bacon</b> <span class="p">1.00</span></li>
          <li><b>Black Pudding</b> <span class="p">1.00</span></li>
          <li><b>Grilled Tomato</b> <span class="p">50c</span></li>
          <li><b>Fried Bread</b> <span class="p">1.00</span></li>
          <li><b>Hash Brown</b> <span class="p">75c</span></li>
          <li><b>Mushrooms</b> <span class="p">1.25</span></li>
          <li><b>2 Bread &amp; Butter</b> <span class="p">1.00</span></li>
          <li><b>Poached Egg</b> <span class="p">1.50</span></li>
          <li><b>Fried Egg</b> <span class="p">75c</span></li>
          <li><b>2 Toast &amp; Butter</b> <span class="p">1.50</span></li>
          <li><b>Scrambled Eggs</b> <span class="p">2.00</span></li>
        </ul>
      </div>
      <div class="panel panel--olive">
        <h3 class="h h--slab h--light">Breakfast SNACKS</h3>
        <ul class="items">
          <li><b>2 fried eggs on toast</b> <span class="p">3.50</span></li>
          <li><b>Scrambled eggs on toast</b> <span class="p">3.50</span></li>
          <li><b>Poached eggs on toast</b> <span class="p">4.00</span></li>
          <li><b>Beans on toast</b> <span class="p">3.50</span></li>
          <li><b>Toast and preserves</b> <span class="p">2.50</span></li>
          <li><b>Sausage sandwich</b> <span class="p">3.00</span></li>
          <li><b>Bacon sandwich</b> <span class="p">4.00</span></li>
          <li><b>Fried Egg sandwich</b> <span class="p">3.50</span></li>
          <li><b>Bacon &amp; Egg sandwich</b> <span class="p">4.50</span></li>
          <li><b>Sausage &amp; Egg sandwich</b> <span class="p">4.50</span></li>
          <li><b>Sausage &amp; Bacon sandwich</b> <span class="p">5.00</span></li>
        </ul>
      </div>
      <div>
        <h3 class="h h--slab">Omelettes</h3>
        <p class="note">served with salad garnish and homemade coleslaw</p>
        <p class="note">Add homemade chips 2.00</p>
        <ul class="items">
          <li><b>Plain</b> <span class="p">5.00</span></li>
          <li><b>Cheddar Cheese</b> <span class="p">5.50</span></li>
          <li><b>Ham</b> <span class="p">5.50</span></li>
          <li><b>Mushroom</b> <span class="p">5.50</span></li>
          <li><b>Cheese &amp; Onion</b> <span class="p">6.00</span></li>
          <li><b>Cheese &amp; Ham</b> <span class="p">6.00</span></li>
          <li><b>Bacon</b> <span class="p">6.00</span></li>
          <li><b>Bacon &amp; Cheese</b> <span class="p">6.50</span></li>
        </ul>
      </div>
      <div class="panel panel--cream">
        <h3 class="h h--slab">Lite Bites <span class="h--maroon">&amp; SIDES</span></h3>
        <ul class="items">
          <li><b>Basket of Homemade Chips</b> <span class="p">3.50</span></li>
          <li><b>Basket of Spicy Wedges</b> <span class="p">3.50</span></li>
          <li><b>Basket of Onion Rings</b> <span class="p">3.50</span></li>
          <li><b>Potato Skins</b> <span class="p">with Cheese &amp; Bacon 4.50</span></li>
          <li><b>Cheesy Chilli Chips</b> <span class="p">6.00</span></li>
          <li><b>Cheesy Chilli Nachos</b> <span class="p">6.50</span></li>
          <li><b>Cheesy Chips</b> <span class="p">4.50</span></li>
          <li><b>Chilli &amp; Chips</b> <span class="p">5.00</span></li>
          <li><b>Curry Sauce &amp; Chips</b> <span class="p">4.50</span></li>
          <li><b>Garlic Bread</b> <span class="p">3.50</span></li>
          <li><b>Toasted Tea-Cake with Jam</b> <span class="p">3.00</span></li>
          <li><b>Fruit Scone with Cream &amp; Jam</b> <span class="p">3.00</span></li>
        </ul>
      </div>
    </div>

    <div class="col col--right">
      <div class="panel panel--cream breakfasts">
        <h3 class="h h--slab">Breakfasts</h3>
        <p class="note intro">All our breakfast ingredients are of the highest quality available, sourced directly from the UK and freshly cooked to order</p>
        <div class="items"><b>Marbrook</b><p class="desc">Bacon, Fried Egg, Sausage, Beans or Grilled Tomato, Toast &amp; Butter, FREE Tea, Coffee or Orange Juice 4.50</p></div>
        <div class="items"><b>Big Feast</b><p class="desc">2 Bacon, 2 Fried Eggs, 2 Sausage, Beans or Grilled Tomato, Toast &amp; Butter, FREE Tea, Coffee or Orange Juice 6.50</p></div>
        <p class="note foot">Any changes made to set breakfasts will be charged as build your own</p>
      </div>

      <div class="rule">
        <h3 class="h">Something <span>Different</span></h3>
        <div class="split items">
          <div>
            <b>Eggs Benedict</b><p class="desc">traditional eggs benedict with home baked ham and soft poached eggs coated in a rich hollandaise sauce on a toasted english muffin 5.50</p>
            <b>Eggs Royale</b><p class="desc">smoked salmon on a toasted english muffin, softly poached eggs and a covering of hollandaise sauce 6.00</p>
            <b>Pancake Stack</b><p class="desc">american style pancakes with crispy bacon and maple syrup 6.50</p>
          </div>
          <div>
            <b>Smoked and Scrambled</b><p class="desc">smoked salmon with creamy scrambled eggs served with wholemeal toast 6.50</p>
            <b>Big Breakfast Wrap</b><p class="desc">sausage, bacon, 2 egg omelette and hash brown served in a soft flour tortilla wrap 5.50</p>
            <b>Breakfast Muffin</b><p class="desc">bacon or sausage on a toasted english muffin with mature cheddar cheese and a perfectly fried egg 5.00</p>
          </div>
        </div>
      </div>

      <div class="split">
        <div class="col">
          <div>
            <h3 class="h">Sandwiches</h3>
            <p class="note">Served with a salad garnish and homemade coleslaw</p>
            <ul class="items">
              <li><b>Mature Cheddar Cheese</b> <span class="p">4.00</span></li>
              <li><b>Bacon &amp; Cheese</b> <span class="p">5.00</span></li>
              <li><b>Home Baked Ham</b> <span class="p">4.50</span></li>
              <li><b>BLT</b> <span class="p">5.00</span></li>
              <li><b>Tuna Mayonnaise</b> <span class="p">4.50</span></li>
              <li><b>Cheese &amp; Home Baked Ham</b> <span class="p">5.00</span></li>
              <li><b>Chicken Mayonnaise</b> <span class="p">4.50</span></li>
              <li><b>Chicken &amp; Bacon Mayonnaise</b> <span class="p">5.50</span></li>
            </ul>
            <p class="note">Any of the above are also available as a floury soft roll or toastie</p>
          </div>
          <div class="panel panel--olive">
            <h3 class="h h--slab h--light">Fresh Baked BAGUETTES</h3>
            <p class="note">served with homemade hand-cut chips, salad and coleslaw</p>
            <ul class="items">
              <li><b>Tuna Cheese Melt</b> <span class="p">7.50</span></li>
              <li><b>Hunters Chicken</b> <span class="p">chicken, bacon, bbq sauce, melted cheese 7.50</span></li>
              <li><b>BLT</b> <span class="p">7.50</span></li>
              <li><b>Chicken Tikka</b> <span class="p">in Minted Mayo 7.50</span></li>
              <li><b>Pork &amp; Herb Sausage</b> <span class="p">with Fried Onion 7.50</span></li>
              <li><b>Chicken &amp; Bacon Mayo</b> <span class="p">7.50</span></li>
            </ul>
          </div>
          <div>
            <h3 class="h h--maroon">Wraps</h3>
            <p class="note">Chicken Breast sautéd with red pepper and onion with crisp lettuce in a Tortilla Wrap</p>
            <ul class="items split">
              <li><b>BBQ</b> <span class="p">6.50</span><br><b>Tikka</b> <span class="p">6.50</span><br><b>Garlic</b> <span class="p">6.50</span></li>
              <li><b>Cajun</b> <span class="p">6.50</span><br><b>Sweet Chilli</b> <span class="p">6.50</span></li>
            </ul>
            <p class="note">add Homemade Chips 2.00</p>
          </div>
        </div>

        <div class="col">
          <div class="panel panel--cream">
            <h3 class="h h--slab">Jacket <span>Potatoes</span></h3>
            <p class="note">served with salad garnish and homemade coleslaw</p>
            <ul class="items">
              <li><b>Plain</b> <span class="p">4.50</span></li>
              <li><b>Baked Beans</b> <span class="p">5.50</span></li>
              <li><b>Cheddar Cheese</b> <span class="p">5.50</span></li>
              <li><b>Tuna Mayonnaise</b> <span class="p">5.50</span></li>
              <li><b>Curry Sauce</b> <span class="p">5.50</span></li>
              <li><b>Beans &amp; Cheese</b> <span class="p">6.00</span></li>
              <li><b>Chicken Curry</b> <span class="p">6.50</span></li>
              <li><b>Chilli</b> <span class="p">6.50</span></li>
            </ul>
          </div>
          <div>
            <h3 class="h">Burgers</h3>
            <ul class="items">
              <li><b>1/2 lb Homemade Aberdeen Angus</b> <span class="p">6.50</span></li>
              <li><b>1/4 lb 100% Irish Beef</b> <span class="p">4.50</span></li>
              <li><b>100% Chicken Breast</b> <span class="p">(battered) 5.00</span></li>
            </ul>
            <p class="note">Add any extra of your choice</p>
            <div class="extras">
              <span>Onion 50c</span><span>Cheddar Cheese 1.00</span>
              <span>Onion Rings 1.00</span><span>Bacon 1.00</span>
              <span>Chilli Con Carne 1.50</span><span>Homemade Chips 2.00</span>
              <span></span><span>Spicy Potato Wedges 2.00</span>
            </div>
            <p class="note">All served with a salad garnish and homemade coleslaw</p>
          </div>
          <div class="panel panel--brown">
            <h3 class="h h--slab h--light">Salads</h3>
            <ul class="items">
              <li><b>Creamy Goats Cheese with Pedro Ximenez Glaze</b> <span class="p">7.00</span></li>
              <li><b>Classic Chicken Caesar &amp; Parmesan Shavings</b> <span class="p">7.00</span></li>
              <li><b>House Mixed Salad with House Dressing</b> <span class="p">6.50</span></li>
            </ul>
          </div>
        </div>
      </div>
    </div>
  </div>
</section>

</body>
</html>
```